Award Winning Patient Support Program needs infographics designed

I need two infographics created for my website and my pitch decks. I have two services I offer. Each service has 6 elements to it. I developed and launched an innovative, coaching-based program to help patients better manage side effects and stress as a solution to a challenge that costs healthcare $600 billion annually and costs patients quality of life and reduces positive outcomes. One of the services, my Patient Adherence Training Program, trains healthcare professionals such as pharmacists, nurses, and doctors, to use coaching skills and a behavior change strategy I designed to help them better listen to, understand, and support patients. The program includes live training intensives, coaching skills development webinars, a customized coaching guide, video training and support documents library, side effect management plan, and confidential patient call review. The second program is my Patient Support Program - it provides patients texting/email support programs, peer mentor support, online group coaching program, side effect management plan, caregiver support, and stress reduction strategies. The program was one of 9 finalists for the 2018 Velmora T9 Pioneering Patient Support Prize and I was invited to resubmit again this year. The goal of the infographics is to visually illustrate the 6 core elements of the two programs. Adherence and behavior change require comprehensive solutions - therefore the programs have to be robust - but I need to simplify the introduction to what each program includes. Patients deserve better support and are often judged as being lazy when they stop taking medication or don't follow "doctor's orders" - when, in fact, it is a complex list of factors that cause non-adherence. My programs also give them skills to help them enjoy better quality of life. The infographic design I envisioned and mocked up uses icons and can include text naming each icon for clarity. I don't expect the infographic to rely on the image of each icon alone. Also, there is one program element that is the same for both - the side effect management plan - so, while there are 12 elements between the two programs, there will be 11 icons. I would need each of the 11 icons in separate files as well as in a file with the finished infographic so I can use the icons independent of the infographic when I go into detailed slides/breakdown of the elements. I have attached a mock up with notes and breaking out the icons. I have also attached the wireframe for the new landing page to show how the infographics will be featured on the web page. My Bright Lantern Path logo was designed using Pixgrove and I still love it and get compliments all the time so I'm turning to this process again and hoping for as great an experience and outcome!

Target Market(s)

Healthcare organizations and pharmaceutical companies

Industry/Entity Type

Pharmaceutical

Font styles to use
Sans Serif

Colors
0792cd
f37122
ffffff

Requirements
Must have
• Consistent design for each icon in the infographic, readable text description of each icon, originally created icons - please do not use the samples in the brief as they are just to give an idea - I do not own the copyright to them.
Should not have
• Don't be insensitive to gender/culture/diversity in choice of icons - needs to be non-specific or a diverse representation

```html
<!DOCTYPE html>
<html lang="en">
<head>
<meta charset="utf-8">
<title>Program Elements Infographics</title>
<link href="https://fonts.googleapis.com/css2?family=Exo:wght@500;600;700&display=swap" rel="stylesheet">
<style>
  :root {
    --brand-orange: #f37122;
    --brand-blue: #0792cd;
    --brand-white: #ffffff;
    --ink: #1f1f1f;
    --frame: #d9d9d9;
    --figure-tone: #d8d3ce;
    --caption-grey: #777777;
  }
  html, body {
    margin: 0;
    padding: 0;
    width: 1200px;
    height: 675px;
    overflow: hidden;
    background: var(--brand-white);
  }
  .canvas {
    display: block;
    width: 1200px;
    height: 675px;
    font-family: "Exo", "Segoe UI", sans-serif;
  }
  .panel-frame { fill: var(--brand-white); stroke: var(--frame); stroke-width: 2; }
  .element-label { font-size: 17px; font-weight: 500; fill: var(--ink); text-anchor: middle; }
  .arc-title { font-size: 42px; font-weight: 700; fill: var(--accent); letter-spacing: 1px; }
  .top-caption { font-size: 14px; fill: var(--caption-grey); text-anchor: middle; }
  .ring-outline { fill: var(--brand-white); stroke: var(--accent); stroke-width: 6; }
  .ring-solid { fill: var(--accent); }
  .icon-accent { color: var(--accent); }
  .icon-white { color: var(--brand-white); }
  .team-figure { fill: var(--figure-tone); }
  .plan-word { font-size: 30px; font-weight: 700; }
  .training-program { --accent: var(--brand-orange); --gear-ink: var(--brand-white); }
  .support-program { --accent: var(--brand-blue); --gear-ink: var(--brand-blue); }
</style>
</head>
<body>
<svg class="canvas" viewBox="0 0 1920 1080" xmlns="http://www.w3.org/2000/svg">
  <defs>
    <!-- Coaching Skills Development Webinars -->
    <symbol id="icon-webinar" viewBox="-100 -100 200 200" overflow="visible">
      <rect x="-74" y="-50" width="148" height="98" rx="6" fill="none" stroke="currentColor" stroke-width="8"/>
      <rect x="-80" y="48" width="160" height="12" rx="4" fill="currentColor"/>
      <path d="M28 -12 v38 h-8 l-6 -10 v20 c4 12 14 14 30 14 c14 0 16 -10 16 -18 v-22 h-8 v12 h-4 v-16 h-8 v14 h-4 v-16 h-8 v16 h-4 v-32 z" fill="currentColor"/>
    </symbol>
    <!-- Live Training Intensives -->
    <symbol id="icon-training" viewBox="-100 -100 200 200" overflow="visible">
      <rect x="-5" y="-68" width="54" height="40" rx="3" fill="none" stroke="currentColor" stroke-width="5"/>
      <line x1="22" y1="-28" x2="22" y2="0" stroke="currentColor" stroke-width="4"/>
      <circle cx="-34" cy="-62" r="7" fill="currentColor"/>
      <rect x="-44" y="-52" width="20" height="26" rx="3" fill="currentColor"/>
      <rect x="-42" y="-28" width="6" height="26" fill="currentColor"/>
      <rect x="-32" y="-28" width="6" height="26" fill="currentColor"/>
      <line x1="-24" y1="-46" x2="-6" y2="-56" stroke="currentColor" stroke-width="3"/>
      <rect x="-66" y="2" width="132" height="7" fill="currentColor"/>
      <g fill="currentColor">
        <circle cx="-44" cy="24" r="9"/><path d="M-62 54 v-10 a18 14 0 0 1 36 0 v10 z"/>
        <circle cx="0" cy="24" r="9"/><path d="M-18 54 v-10 a18 14 0 0 1 36 0 v10 z"/>
        <circle cx="44" cy="24" r="9"/><path d="M26 54 v-10 a18 14 0 0 1 36 0 v10 z"/>
      </g>
    </symbol>
    <!-- Customized Coaching Guide -->
    <symbol id="icon-guide" viewBox="-100 -100 200 200" overflow="visible">
      <g transform="rotate(-4)">
        <path d="M-52 -62 h100 v132 h-100 z" fill="currentColor"/>
        <path d="M-56 -66 l86 -8" stroke="currentColor" stroke-width="5" fill="none"/>
        <g fill="none" stroke="var(--gear-ink)">
          <circle cx="-12" cy="-6" r="14" stroke-width="8"/>
          <circle cx="-12" cy="-6" r="21" stroke-width="7" stroke-dasharray="6 5"/>
          <circle cx="24" cy="24" r="10" stroke-width="6"/>
          <circle cx="24" cy="24" r="16" stroke-width="6" stroke-dasharray="5 4"/>
        </g>
      </g>
    </symbol>
    <!-- Video Training Library -->
    <symbol id="icon-video" viewBox="-100 -100 200 200" overflow="visible">
      <g fill="none" stroke="currentColor" stroke-width="5">
        <rect x="-20" y="-56" width="74" height="92" rx="4"/>
        <rect x="-30" y="-48" width="74" height="92" rx="4"/>
        <rect x="-40" y="-40" width="74" height="92" rx="4"/>
      </g>
      <rect x="-56" y="-26" width="84" height="88" rx="5" fill="currentColor"/>
      <rect x="-46" y="-4" width="64" height="44" fill="var(--gear-ink)"/>
      <path d="M-20 8 l16 10 l-16 10 z" fill="currentColor"/>
    </symbol>
    <!-- Confidential Patient Call Review -->
    <symbol id="icon-review" viewBox="-100 -100 200 200" overflow="visible">
      <g fill="none" stroke="currentColor" stroke-width="6" stroke-linejoin="round">
        <path d="M-62 -56 h56 v44 h-30 l-12 10 v-10 h-14 z"/>
        <path d="M6 -40 h56 v44 h-14 v10 l-12 -10 h-30 z"/>
        <path d="M-44 -22 v-16 h6 l6 -10 v10 h10 v16 z"/>
        <path d="M24 -34 v16 h6 l6 10 v-10 h10 v-16 z"/>
        <circle cx="0" cy="26" r="16"/>
        <path d="M-28 70 v-10 a28 22 0 0 1 56 0 v10"/>
      </g>
    </symbol>
    <!-- Side Effect Management Plan -->
    <symbol id="icon-plan" viewBox="-100 -100 200 200" overflow="visible">
      <g transform="rotate(-16)">
        <rect x="-52" y="-66" width="104" height="136" fill="currentColor"/>
        <text x="-40" y="-30" class="plan-word" fill="var(--gear-ink)">Plan</text>
        <g stroke="var(--gear-ink)" stroke-width="4">
          <line x1="-40" y1="-12" x2="40" y2="-12"/><line x1="-40" y1="0" x2="40" y2="0"/>
          <line x1="-40" y1="12" x2="40" y2="12"/><line x1="-40" y1="24" x2="40" y2="24"/>
          <line x1="-40" y1="36" x2="40" y2="36"/><line x1="-40" y1="48" x2="40" y2="48"/>
          <line x1="-40" y1="60" x2="40" y2="60"/>
        </g>
      </g>
    </symbol>
    <!-- Online Group Coaching Program -->
    <symbol id="icon-group-coaching" viewBox="-100 -100 200 200" overflow="visible">
      <rect x="-74" y="-50" width="148" height="98" rx="6" fill="none" stroke="currentColor" stroke-width="8"/>
      <rect x="-80" y="48" width="160" height="12" rx="4" fill="currentColor"/>
      <g fill="currentColor">
        <circle cx="-38" cy="-10" r="10"/><path d="M-56 34 v-8 a18 16 0 0 1 36 0 v8 z"/>
        <circle cx="0" cy="-16" r="12"/><path d="M-21 34 v-10 a21 18 0 0 1 42 0 v10 z"/>
        <circle cx="38" cy="-10" r="10"/><path d="M20 34 v-8 a18 16 0 0 1 36 0 v8 z"/>
      </g>
    </symbol>
    <!-- Texting / Email Support -->
    <symbol id="icon-texting" viewBox="-100 -100 200 200" overflow="visible">
      <rect x="-64" y="-62" width="56" height="112" rx="9" fill="none" stroke="currentColor" stroke-width="7"/>
      <line x1="-46" y1="36" x2="-26" y2="36" stroke="currentColor" stroke-width="5" stroke-linecap="round"/>
      <rect x="-54" y="-46" width="34" height="18" rx="4" fill="currentColor"/>
      <rect x="-52" y="-18" width="34" height="18" rx="4" fill="currentColor"/>
      <rect x="6" y="-22" width="62" height="46" rx="4" fill="none" stroke="currentColor" stroke-width="6"/>
      <path d="M8 -18 L37 6 L66 -18" fill="none" stroke="currentColor" stroke-width="6" stroke-linejoin="round"/>
    </symbol>
    <!-- Peer Mentor Support -->
    <symbol id="icon-mentor" viewBox="-100 -100 200 200" overflow="visible">
      <g fill="currentColor">
        <circle cx="-30" cy="-16" r="17"/>
        <path d="M-62 54 v-14 a32 28 0 0 1 64 0 v14 z"/>
        <circle cx="32" cy="2" r="13"/>
        <path d="M8 54 v-8 a24 22 0 0 1 48 0 v8 z"/>
        <path d="M12 -30 c-12 -9 -18 -18 -10 -25 c5 -4 10 -1 10 4 c0 -5 5 -8 10 -4 c8 7 2 16 -10 25 z"/>
      </g>
    </symbol>
    <!-- Caregiver Support -->
    <symbol id="icon-caregiver" viewBox="-100 -100 200 200" overflow="visible">
      <path d="M0 -4 c-30 -22 -42 -44 -22 -58 c10 -6 22 0 22 10 c0 -10 12 -16 22 -10 c20 14 8 36 -22 58 z" fill="currentColor"/>
      <path d="M-72 18 h24 l28 10 h32 a8 8 0 0 1 0 16 h-28 h30 l32 -20 a8 8 0 0 1 10 12 l-42 34 h-62 l-10 -6 h-14 z" fill="currentColor"/>
    </symbol>
    <!-- Stress Reduction Strategies -->
    <symbol id="icon-stress" viewBox="-100 -100 200 200" overflow="visible">
      <g fill="currentColor">
        <path d="M0 -64 c-20 24 -20 50 0 66 c20 -16 20 -42 0 -66 z"/>
        <path d="M-8 8 c-30 -4 -50 -24 -54 -48 c26 4 44 22 50 44 z"/>
        <path d="M8 8 c30 -4 50 -24 54 -48 c-26 4 -44 22 -50 44 z"/>
      </g>
      <g fill="none" stroke="currentColor" stroke-width="6" stroke-linecap="round">
        <path d="M-60 30 q15 -10 30 0 t30 0 t30 0 t30 0"/>
        <path d="M-48 50 q12 -8 24 0 t24 0 t24 0 t24 0"/>
      </g>
    </symbol>
    <path id="arc-left" d="M394 190 A 96 96 0 0 1 556 190"/>
    <path id="arc-right" d="M1344 196 A 96 96 0 0 1 1506 196"/>
  </defs>

  <text class="top-caption" x="1510" y="2">Stress Reduction Strategies</text>

  <!-- Patient Adherence Training Program -->
  <g class="program-panel training-program">
    <rect class="panel-frame" x="28" y="72" width="918" height="926"/>
    <text class="arc-title"><textPath href="#arc-left" startOffset="50%" text-anchor="middle">WEBINAR</textPath></text>

    <rect class="team-figure" x="325" y="415" width="295" height="300" rx="30" role="img" aria-label="Illustration of a diverse group of healthcare professionals standing together"/>

    <circle class="ring-outline" cx="474" cy="262" r="95"/>
    <use class="icon-accent" href="#icon-webinar" x="374" y="162" width="200" height="200"/>
    <text class="element-label" x="474" y="379">Coaching Skills Development Webinars</text>

    <circle class="ring-outline" cx="207" cy="409" r="95"/>
    <use class="icon-accent" href="#icon-training" x="107" y="309" width="200" height="200"/>
    <text class="element-label" x="207" y="530">Live Training Intensives</text>

    <circle class="ring-outline" cx="751" cy="409" r="95"/>
    <use class="icon-accent" href="#icon-guide" x="651" y="309" width="200" height="200"/>
    <text class="element-label" x="751" y="529">Customized Coaching Guide</text>

    <circle class="ring-outline" cx="215" cy="697" r="95"/>
    <use class="icon-accent" href="#icon-video" x="115" y="597" width="200" height="200"/>
    <text class="element-label" x="215" y="817">Video Training Library</text>

    <circle class="ring-outline" cx="740" cy="697" r="95"/>
    <use class="icon-accent" href="#icon-review" x="640" y="597" width="200" height="200"/>
    <text class="element-label" x="740" y="823">Confidential Patient Call Review</text>

    <circle class="ring-outline" cx="469" cy="838" r="95"/>
    <use class="icon-accent" href="#icon-plan" x="369" y="738" width="200" height="200"/>
    <text class="element-label" x="474" y="964">Side Effect Management Plan</text>
  </g>

  <!-- Patient Support Program -->
  <g class="program-panel support-program">
    <rect class="panel-frame" x="978" y="80" width="918" height="926"/>
    <text class="arc-title"><textPath href="#arc-right" startOffset="50%" text-anchor="middle">ONLINE</textPath></text>

    <rect class="team-figure" x="1275" y="422" width="295" height="300" rx="30" role="img" aria-label="Illustration of a diverse group of patients and caregivers standing together"/>

    <circle class="ring-solid" cx="1424" cy="268" r="98"/>
    <use class="icon-white" href="#icon-group-coaching" x="1324" y="168" width="200" height="200"/>
    <text class="element-label" x="1424" y="388">Online Group Coaching Program</text>

    <circle class="ring-solid" cx="1157" cy="417" r="98"/>
    <use class="icon-white" href="#icon-texting" x="1057" y="317" width="200" height="200"/>
    <text class="element-label" x="1157" y="539">Texting / Email Support</text>

    <circle class="ring-solid" cx="1701" cy="417" r="98"/>
    <use class="icon-white" href="#icon-mentor" x="1601" y="317" width="200" height="200"/>
    <text class="element-label" x="1701" y="537">Peer Mentor Support</text>

    <circle class="ring-solid" cx="1165" cy="706" r="98"/>
    <use class="icon-white" href="#icon-caregiver" x="1065" y="606" width="200" height="200"/>
    <text class="element-label" x="1165" y="826">Caregiver Support</text>

    <circle class="ring-solid" cx="1689" cy="706" r="98"/>
    <use class="icon-white" href="#icon-stress" x="1589" y="606" width="200" height="200"/>
    <text class="element-label" x="1689" y="831">Stress Reduction Strategies</text>

    <circle class="ring-solid" cx="1419" cy="847" r="98"/>
    <use class="icon-white" href="#icon-plan" x="1319" y="747" width="200" height="200"/>
    <text class="element-label" x="1424" y="972">Side Effect Management Plan</text>
  </g>
</svg>
</body>
</html>
```